Natural healthcare clinic needs stationery and business card design

We have had a logo developed by Pixel Harbor and are now looking at utilising it for a new business concept. The concept is a natural healthcare clinic that hosts a number of small businesses. The individual practitioners may want to utilise the host business stationery to provide a consistent message to clients.

I am looking for a stationery design - letterhead, DL brochure template and business card that uses our logo. The business name 'Verdant Tides' is all about getting rhythm back into your life so you can be fit and healthy. The stationery design should reflect this.

There are a couple of requirements for the business card, it needs to be double-sided with black and white back. There should be lines to write appointment times on. The cards may need to be custom named on the front for example Marcia Tolk, Remedial Therapist and Aromatherapist. Therefore if a template can be provided so we can customise this information using MS Publisher, it would be appreciated.

The DL brochure template needs to be A4 folded to DL. I am looking for a consistent brand message that can be utilised to produce our own clinic brochures.

The natural healthcare clinic will host the following types of businesses - remedial massage, pregnancy massage, oncology massage, aromatherapy, acupuncture - as a bit of a guide.

Target Market(s)

25-45 year old male and females who work full time.

Industry/Entity Type

Healthcare

Requirements
Must have
• Use the logo I have already.

```html
<!DOCTYPE html>
<html lang="en">
<head>
<meta charset="utf-8">
<title>Verdant Tides – Stationery Presentation</title>
<link href="https://fonts.googleapis.com/css2?family=Open+Sans:wght@400;600;700&family=PT+Sans:wght@400;700&display=swap" rel="stylesheet">
<style>
:root{
  --board:#7a4f2c;
  --label:#ffffff;
  --paper:#ffffff;
  --green:#7f9a34;
  --green-light:#9cc43a;
  --olive:#84923f;
  --brown:#5b4a2d;
  --ink:#4a4a4a;
  --red:#e1262d;
  --blue:#2e3192;
  --stripe-red:#d9232d;
  --stripe-blue:#3a8ac6;
}
*{box-sizing:border-box;margin:0;padding:0}
html,body{width:1200px;height:963px;overflow:hidden}
body{background:var(--board);font-family:"Open Sans",Arial,sans-serif;position:relative;color:var(--ink)}
.board-label{position:absolute;color:var(--label);font-family:"PT Sans",Arial,sans-serif;font-weight:700;font-size:18px}
.sheet{position:absolute;background:var(--paper);overflow:hidden;box-shadow:2px 3px 8px rgba(0,0,0,.45)}
.brand-name{font-family:"Open Sans",Arial,sans-serif;font-weight:400;color:var(--green);white-space:nowrap;display:flex;align-items:center;gap:6px}
.brand-dot{display:inline-block;border-radius:50%;background:var(--green-light)}
.corner-stripes,.swoosh{position:absolute;display:block}
.contact{position:absolute;font-size:8.5px;line-height:13px;color:var(--ink);z-index:2}
.contact li{list-style:none;display:flex;align-items:center;gap:4px}
.contact svg{width:8px;height:8px;fill:var(--ink)}
.photo{position:absolute}

/* letterhead */
.letterhead{left:51px;top:77px;width:514px;height:663px}
.letterhead .brand-name{position:absolute;left:38px;top:92px;font-size:23px}
.letterhead .divider{position:absolute;left:220px;top:60px;width:1px;height:52px;background:var(--green-light)}
.letterhead .contact{left:240px;top:58px}
.letterhead .address{margin-top:4px}
.letterhead .clinic{position:absolute;right:42px;bottom:12px;color:#fff;font-family:"PT Sans",Arial,sans-serif;font-size:15px}

/* brochure inside panel */
.panel-services{left:597px;top:78px;width:251px;height:706px}
.panel-services .photo{left:0;top:0;width:251px;height:180px;background:linear-gradient(135deg,#f0d2b8 0%,#c9876a 45%,#a8302f 100%)}
.panel-services .body{position:absolute;left:0;top:168px;width:251px;height:440px;background:var(--olive)}
.panel-services .headline{position:absolute;left:19px;top:44px;color:#fff;font-family:"PT Sans",Arial,sans-serif;font-weight:700;font-size:17.5px;line-height:23px}
.service{position:absolute;left:0;width:251px}
.service h3{display:block;width:165px;height:20px;line-height:20px;padding-left:19px;color:#fff;font-family:"PT Sans",Arial,sans-serif;font-size:13px;font-weight:700;background:var(--green-light);clip-path:polygon(0 0,93% 0,100% 50%,93% 100%,0 100%)}
.service p{margin:8px 18px 0 18px;color:#fff;font-size:6.6px;line-height:9.6px;text-align:justify}
.panel-services .brand-name{position:absolute;right:18px;top:640px;font-size:15px}
.panel-services .tagline{position:absolute;left:130px;top:662px;font-size:8px;color:var(--brown)}
.panel-services .contact{left:14px;top:656px;font-size:7.5px;line-height:12px}
.panel-services .address{position:absolute;right:14px;top:680px;font-size:7.5px;line-height:10px;color:var(--ink);font-weight:600}

/* brochure cover */
.panel-cover{left:865px;top:78px;width:249px;height:706px;background:linear-gradient(90deg,#e9e9e9,#ffffff 50%,#e9e9e9)}
.panel-cover .title{position:absolute;top:12px;width:100%;text-align:center;color:var(--red);font-family:"PT Sans",Arial,sans-serif;font-weight:700;font-size:20px;line-height:22px}
.panel-cover .services{position:absolute;top:65px;width:100%;text-align:center;color:var(--blue);font-family:"PT Sans",Arial,sans-serif;font-weight:700;font-size:13px;line-height:17px;padding:0 22px}
.panel-cover .brand-name{position:absolute;left:18px;top:262px;font-size:26px}
.panel-cover .tagline{position:absolute;left:19px;top:300px;font-size:10px;color:var(--brown)}
.panel-cover .intro{position:absolute;left:19px;top:328px;width:212px;font-size:8px;line-height:11.5px;text-align:justify}
.panel-cover .photo{left:18px;width:214px;height:124px;border-radius:8px;box-shadow:0 2px 4px rgba(0,0,0,.4)}
.panel-cover .photo-one{top:372px;background:linear-gradient(135deg,#f6c07a,#e49a53 50%,#c86f3a)}
.panel-cover .photo-two{top:508px;background:linear-gradient(135deg,#f6efe9,#e5b994 55%,#c88a63)}
.panel-cover .phone{position:absolute;right:18px;top:658px;color:#fff;font-family:"PT Sans",Arial,sans-serif;font-weight:700;font-size:16px}
.panel-cover .web{position:absolute;right:18px;top:684px;color:#fff;font-size:8.5px;font-weight:700;letter-spacing:1.3px}

/* business cards */
.card-front{left:51px;top:782px;width:212px;height:120px}
.card-front .brand-name{position:absolute;left:10px;top:50px;font-size:13px}
.card-front .tagline{position:absolute;left:11px;top:70px;font-size:7px;color:var(--brown)}
.card-front .holder{position:absolute;left:128px;top:11px;color:var(--brown);font-size:8.5px;line-height:10px}
.card-front .holder small{font-size:6px;display:block}
.card-front .contact{left:128px;top:94px;font-size:5px;line-height:7px;color:#fff}
.card-front .contact svg{width:5px;height:5px;fill:#fff}

.card-back{left:279px;top:782px;width:211px;height:120px}
.card-back .lines{position:absolute;left:16px;top:17px;width:180px}
.card-back .lines span{display:block;height:1px;background:var(--green-light);margin-bottom:16px}
.card-back .address{position:absolute;left:92px;top:70px;font-size:5px;color:var(--ink)}
.card-back .appointment{position:absolute;left:12px;top:94px;color:#fff;font-size:9px;line-height:11px;font-weight:700;z-index:2}
.card-back .appointment span{font-weight:400;font-size:7.5px;display:block}
</style>
</head>
<body>

<div class="board-label" style="left:53px;top:37px">Letterhead option 4a (Dec 12)</div>
<div class="board-label" style="left:775px;top:37px">brochure option 4</div>

<section class="sheet letterhead">
  <svg class="corner-stripes" width="80" height="50" viewBox="0 0 80 50" style="left:0;top:0">
    <path d="M0 44 Q14 8 78 2" fill="none" stroke="var(--stripe-red)" stroke-width="2.5"/>
    <path d="M0 48 Q18 12 80 6" fill="none" stroke="var(--stripe-blue)" stroke-width="2"/>
    <path d="M0 50 Q22 16 80 10" fill="none" stroke="var(--green-light)" stroke-width="3"/>
  </svg>
  <div class="brand-name"><span class="brand-dot" style="width:12px;height:12px"></span>Verdant Tides</div>
  <div class="divider"></div>
  <ul class="contact">
    <li><svg viewBox="0 0 10 10"><path d="M2 0h2l1 3-1.5 1a6 6 0 0 0 2.5 2.5L7 5l3 1v2c0 1-1 2-2 2A8 8 0 0 1 0 2c0-1 1-2 2-2z"/></svg>012.345.6789</li>
    <li><svg viewBox="0 0 10 10"><path d="M0 2h10v6H0z"/></svg>info@verdanttides.com</li>
    <li><svg viewBox="0 0 10 10"><circle cx="5" cy="5" r="5"/></svg>www.verdanttides.com</li>
    <li class="address">Suite 000, City name, Country name 00000</li>
  </ul>
  <svg class="swoosh" width="514" height="90" viewBox="0 0 514 90" style="left:0;bottom:0">
    <path d="M0 38 Q220 10 514 22" fill="none" stroke="var(--brown)" stroke-width="1.2"/>
    <path d="M0 52 Q250 14 514 26 L514 90 L0 90 Z" fill="var(--green)"/>
    <path d="M0 52 Q250 14 514 26 L514 36 Q260 28 0 62 Z" fill="var(--green-light)"/>
  </svg>
  <div class="clinic">Well Being Clinic</div>
</section>

<section class="sheet panel-services">
  <div class="photo" role="img" aria-label="Photo of a smiling client receiving a shoulder massage"></div>
  <div class="body">
    <svg class="swoosh" width="251" height="30" viewBox="0 0 251 30" style="left:0;top:-14px">
      <path d="M0 14 Q120 -4 251 10 L251 30 L0 30 Z" fill="var(--olive)"/>
      <path d="M0 18 Q120 2 251 14" fill="none" stroke="#fff" stroke-width="1"/>
    </svg>
    <div class="headline">Lorem Ipsum Dolor sit<br>Consectetur adipisicing</div>
    <div class="service" style="top:120px">
      <h3>Remedial Massage</h3>
      <p>Lorem ipsum dolor sit amet, consectetur adipisicing elit, sed do eiusmod tempor incididunt ut labore et dolore magna aliqua. Ut enim ad minim veniam, quis nostrud exercitation ullamco laboris nisi ut aliquip ex ea commodo consequat. Duis aute irure dolor in reprehenderit in voluptate velit esse cillum dolore eu fugiat nulla pariatur.</p>
    </div>
    <div class="service" style="top:214px">
      <h3>Pregnancy Massage</h3>
      <p>Lorem ipsum dolor sit amet, consectetur adipisicing elit, sed do eiusmod tempor incididunt ut labore et dolore magna aliqua. Ut enim ad minim veniam, quis nostrud exercitation ullamco laboris nisi ut aliquip ex ea commodo consequat. Duis aute irure dolor in reprehenderit in voluptate velit esse cillum dolore eu fugiat nulla pariatur. Excepteur sint occaecat cupidatat non proident.</p>
    </div>
    <div class="service" style="top:314px">
      <h3>Oncology Massage</h3>
      <p>Lorem ipsum dolor sit amet, consectetur adipisicing elit, sed do eiusmod tempor incididunt ut labore et dolore magna aliqua. Ut enim ad minim veniam, quis nostrud exercitation ullamco laboris nisi ut aliquip ex ea commodo consequat. Duis aute irure dolor in reprehenderit in voluptate velit esse cillum dolore eu fugiat nulla pariatur. Excepteur sint occaecat cupidatat non proident, sunt in culpa qui officia deserunt mollit anim id est laborum.</p>
    </div>
  </div>
  <svg class="swoosh" width="251" height="40" viewBox="0 0 251 40" style="left:0;top:596px">
    <path d="M0 0 H251 V8 Q130 30 0 16 Z" fill="var(--olive)"/>
    <path d="M0 22 Q130 36 251 12" fill="none" stroke="var(--brown)" stroke-width="1"/>
    <path d="M0 26 Q130 40 251 16" fill="none" stroke="var(--green-light)" stroke-width="1.5"/>
  </svg>
  <div class="brand-name"><span class="brand-dot" style="width:8px;height:8px"></span>Verdant Tides</div>
  <div class="tagline">Well Being Clinic</div>
  <ul class="contact">
    <li><svg viewBox="0 0 10 10"><path d="M2 0h2l1 3-1.5 1a6 6 0 0 0 2.5 2.5L7 5l3 1v2c0 1-1 2-2 2A8 8 0 0 1 0 2c0-1 1-2 2-2z"/></svg>012.345.6789</li>
    <li><svg viewBox="0 0 10 10"><path d="M0 2h10v6H0z"/></svg>info@verdanttides.com</li>
    <li><svg viewBox="0 0 10 10"><circle cx="5" cy="5" r="5"/></svg>www.verdanttides.com</li>
  </ul>
  <div class="address">Suite 000, City name<br>Country name 00000</div>
</section>

<section class="sheet panel-cover">
  <svg class="corner-stripes" width="60" height="40" viewBox="0 0 60 40" style="left:0;top:0">
    <path d="M0 34 Q10 6 58 1" fill="none" stroke="var(--stripe-red)" stroke-width="2"/>
    <path d="M0 38 Q14 10 60 5" fill="none" stroke="var(--stripe-blue)" stroke-width="1.5"/>
    <path d="M0 40 Q18 14 60 9" fill="none" stroke="var(--green-light)" stroke-width="2.5"/>
  </svg>
  <h1 class="title">Lorem<br>Ipsum Dolor sit</h1>
  <p class="services">Marcia Tolk, Remedial Massage Pregnancy Massage, Oncology Massage, Aromatherapy, Acupuncture</p>
  <div class="brand-name"><span class="brand-dot" style="width:14px;height:14px"></span>Verdant Tides</div>
  <div class="tagline">Well Being Clinic</div>
  <p class="intro">Lorem ipsum dolor sit amet, consectetur adipisicing elit, sed do eiusmod tempor incididunt ut labore et dolore magna aliqua. Ut enim ad minim veniam.</p>
  <div class="photo photo-one" role="img" aria-label="Close-up photo of hands massaging a back"></div>
  <div class="photo photo-two" role="img" aria-label="Photo of a client relaxing during a back massage"></div>
  <svg class="swoosh" width="249" height="80" viewBox="0 0 249 80" style="left:0;bottom:0">
    <path d="M0 16 Q120 0 249 6" fill="none" stroke="var(--brown)" stroke-width="1"/>
    <path d="M0 26 Q120 4 249 10 L249 80 L0 80 Z" fill="var(--green)"/>
    <path d="M0 26 Q120 4 249 10 L249 18 Q120 14 0 34 Z" fill="var(--green-light)"/>
  </svg>
  <div class="phone">012.345.6789</div>
  <div class="web">www.verdanttides.com</div>
</section>

<section class="sheet card-front">
  <svg class="corner-stripes" width="40" height="28" viewBox="0 0 40 28" style="left:0;top:0">
    <path d="M0 24 Q8 4 38 1" fill="none" stroke="var(--stripe-red)" stroke-width="1.5"/>
    <path d="M0 26 Q10 6 40 3" fill="none" stroke="var(--stripe-blue)" stroke-width="1"/>
    <path d="M0 28 Q12 8 40 6" fill="none" stroke="var(--green-light)" stroke-width="2"/>
  </svg>
  <div class="brand-name"><span class="brand-dot" style="width:7px;height:7px"></span>Verdant Tides</div>
  <div class="tagline">Well Being Clinic</div>
  <div class="holder">YOUR NAME<small>Director</small></div>
  <svg class="swoosh" width="212" height="52" viewBox="0 0 212 52" style="left:0;bottom:0">
    <path d="M0 14 Q110 18 212 -4" fill="none" stroke="var(--brown)" stroke-width="1"/>
    <path d="M0 20 Q110 22 212 0 L212 6 Q110 28 0 26 Z" fill="var(--green-light)"/>
    <path d="M0 26 Q110 28 212 6 L212 52 L0 52 Z" fill="var(--green)"/>
  </svg>
  <ul class="contact">
    <li><svg viewBox="0 0 10 10"><circle cx="5" cy="5" r="5"/></svg>012.345.6789</li>
    <li><svg viewBox="0 0 10 10"><circle cx="5" cy="5" r="5"/></svg>info@verdanttides.com</li>
    <li><svg viewBox="0 0 10 10"><circle cx="5" cy="5" r="5"/></svg>www.verdanttides.com</li>
  </ul>
</section>

<section class="sheet card-back">
  <div class="lines"><span></span><span></span><span></span><span></span></div>
  <div class="address">Suite 000, City name, Country name 00000</div>
  <svg class="swoosh" width="211" height="52" viewBox="0 0 211 52" style="left:0;bottom:0">
    <path d="M0 4 Q100 24 211 12" fill="none" stroke="var(--brown)" stroke-width="1"/>
    <path d="M0 8 Q100 28 211 16 L211 22 Q100 34 0 14 Z" fill="var(--green-light)"/>
    <path d="M0 14 Q100 34 211 22 L211 52 L0 52 Z" fill="var(--green)"/>
  </svg>
  <div class="appointment">Appointment<span>Well Being Clinic</span></div>
</section>

</body>
</html>
```